Vantrel Ashcombe LLC

we need a business card design

Industry/Entity Type

hvac

Contact Information for Business Card

my logo

Requirements
Must have
• my logo and same colors

```html
<!DOCTYPE html>
<html lang="en">
<head>
<meta charset="utf-8">
<title>Vantrel Ashcombe LLC – Business Card</title>
<link href="https://fonts.googleapis.com/css2?family=Poppins:wght@400;600;700&display=swap" rel="stylesheet">
<style>
  :root {
    --backdrop: #979797;
    --brand-blue: #0560a6;
    --brand-cyan: #0aa8dc;
    --card-white: #ffffff;
    --text-grey: #555555;
    --rule-grey: #777777;
    --pin-orange: #f06a45;
  }
  * { margin: 0; padding: 0; box-sizing: border-box; }
  html, body {
    width: 1200px;
    height: 1000px;
    overflow: hidden;
    background: var(--backdrop);
    font-family: "Poppins", sans-serif;
  }
  .card {
    position: absolute;
    left: 211px;
    width: 778px;
    height: 448px;
  }
  .card--front {
    top: 35px;
    background: var(--brand-blue);
  }
  .card--back {
    top: 517px;
    background: var(--card-white);
  }
  .brand-name {
    position: absolute;
    left: 0;
    width: 100%;
    text-align: center;
    font-weight: 700;
    letter-spacing: 0.5px;
  }
  .card--front .brand-name {
    top: 170px;
    font-size: 40px;
    color: var(--card-white);
  }
  .card--back .brand-name {
    top: 110px;
    font-size: 30px;
    color: var(--brand-blue);
  }
  .holder {
    position: absolute;
    right: 390px;
    top: 264px;
    text-align: right;
  }
  .holder__name {
    font-size: 29px;
    font-weight: 700;
    line-height: 1.2;
    color: var(--brand-blue);
  }
  .holder__name span { color: var(--brand-cyan); }
  .holder__title {
    margin-top: 2px;
    font-size: 13px;
    letter-spacing: 4px;
    color: var(--text-grey);
    margin-right: -4px;
  }
  .divider {
    position: absolute;
    left: 388px;
    top: 247px;
    width: 1.5px;
    height: 92px;
    background: var(--rule-grey);
  }
  .contacts {
    position: absolute;
    left: 406px;
    top: 255px;
    list-style: none;
  }
  .contacts li {
    display: flex;
    align-items: center;
    height: 29px;
    font-size: 19px;
    color: var(--text-grey);
  }
  .contacts svg {
    width: 16px;
    height: 16px;
    margin-right: 9px;
    flex-shrink: 0;
  }
  .location {
    position: absolute;
    left: 0;
    width: 100%;
    top: 395px;
    display: flex;
    justify-content: center;
    align-items: center;
    font-size: 17px;
    color: var(--text-grey);
  }
  .location svg {
    width: 22px;
    height: 28px;
    margin-right: 6px;
  }
</style>
</head>
<body>
  <section class="card card--front">
    <p class="brand-name">Vantrel Ashcombe LLC</p>
  </section>

  <section class="card card--back">
    <p class="brand-name">Vantrel Ashcombe LLC</p>

    <div class="holder">
      <p class="holder__name">Name <span>Surname</span></p>
      <p class="holder__title">TITLE</p>
    </div>

    <div class="divider"></div>

    <ul class="contacts">
      <li>
        <svg viewBox="0 0 16 16" aria-hidden="true"><path d="M4 1.5 6 4.5 4.8 6.2c.8 1.9 2.3 3.6 4.3 4.6l1.4-1.3 3 2-1 2.5C7.5 14 2 8.5 1.8 2.7Z" fill="none" stroke="var(--brand-cyan)" stroke-width="1.6" stroke-linejoin="round"/></svg>
        555-014-2290
      </li>
      <li>
        <svg viewBox="0 0 16 16" aria-hidden="true"><rect x="1" y="3.5" width="14" height="9.5" fill="none" stroke="var(--brand-cyan)" stroke-width="1.4"/><path d="M1 3.5 8 9l7-5.5M1 13l5-4.5M15 13l-5-4.5" fill="none" stroke="var(--brand-cyan)" stroke-width="1.2"/></svg>
        milo@northfieldaircompany.com
      </li>
      <li>
        <svg viewBox="0 0 16 16" aria-hidden="true"><circle cx="8" cy="8" r="6.5" fill="none" stroke="var(--brand-cyan)" stroke-width="1.3"/><ellipse cx="8" cy="8" rx="3" ry="6.5" fill="none" stroke="var(--brand-cyan)" stroke-width="1.1"/><path d="M1.5 8h13M2.5 4.8h11M2.5 11.2h11" stroke="var(--brand-cyan)" stroke-width="1.1"/></svg>
        vantrelashcombe.com
      </li>
    </ul>

    <div class="location">
      <svg viewBox="0 0 22 28" aria-hidden="true"><ellipse cx="8" cy="25" rx="7" ry="1.8" fill="#bbbbbb"/><path d="M12 1a8 8 0 0 0-8 8c0 6 8 15 8 15s8-9 8-15a8 8 0 0 0-8-8Z" fill="var(--pin-orange)"/><circle cx="12" cy="9" r="3" fill="var(--card-white)"/></svg>
      Harbor Point, FL, USA
    </div>
  </section>
</body>
</html>
```